New to ArtHarbor? This Contest is for you!

Are you new to ArtHarbor and looking to enter your first contest? Look no further! We're launching this special contest to help you get started on building a design portfolio at ArtHarbor!

Requirements:
* Create a beautiful and eye-catching graphic design which includes the words "Spot me at ArtHarbor!"
* Upload your design to this contest AND share it on Chatterly
* You must upload your entry before 12:00am 1 April
* This must be your very FIRST entry on ArtHarbor to be eligible to receive a prize. If you've already entered other ArtHarbor contests you won't be eligible to win the prizes
* Your design must adhere to our quality standards to be eligible to receive a prize

Prizes:
* There are 150 x $5 participation payments ($750) available to be awarded to high-quality designs
* First prize for the best design is $150
* Second prize is $100

Requirements
Must have
• Your design must contain the words "Spot me at ArtHarbor".
• This must be your first entry on ArtHarbor to be eligible for the prizes.
• Your design must adhere to our quality standards.
Should not have
• No stock images or overused concepts.

```html
<!DOCTYPE html>
<html lang="en">
<head>
<meta charset="utf-8">
<title>Spot me at ArtHarbor</title>
<link rel="stylesheet" href="https://fonts.googleapis.com/css2?family=Oswald:wght@400&display=swap">
<style>
  :root {
    --paper: #ffffff;
    --pencil-red: #e21b23;
    --stylus-dark: #3a3b3d;
    --caption-ink: #111111;
  }
  html, body {
    margin: 0;
    padding: 0;
    overflow: hidden;
    background: var(--paper);
  }
  .canvas {
    position: relative;
    width: 1200px;
    height: 1200px;
    background: var(--paper);
    overflow: hidden;
  }
  .pencil-row {
    position: absolute;
    left: 55px;
    display: grid;
    grid-template-columns: repeat(12, 16px);
    column-gap: 80px;
    align-items: start;
  }
  .pencil-row--top { top: 24px; }
  .pencil-row--middle { top: 395px; }
  .pencil-row--bottom { top: 787px; }
  .pencil {
    width: 16px;
    height: 326px;
    background: var(--pencil-red);
    border-radius: 2px;
  }
  .stylus {
    justify-self: center;
    width: 37px;
    height: 336px;
    margin-top: 4px;
    background: var(--stylus-dark);
    border-radius: 16px 16px 10px 10px;
  }
  .caption {
    position: absolute;
    right: 51px;
    top: 1140px;
    margin: 0;
    font-family: "Oswald", "Arial Narrow", sans-serif;
    font-weight: 400;
    font-size: 19px;
    letter-spacing: 0.3px;
    text-transform: uppercase;
    color: var(--caption-ink);
  }
</style>
</head>
<body>
<main class="canvas">
  <div class="pencil-row pencil-row--top">
    <div class="pencil" role="img" aria-label="Red pencil"></div>
    <div class="pencil" role="img" aria-label="Red pencil"></div>
    <div class="pencil" role="img" aria-label="Red pencil"></div>
    <div class="pencil" role="img" aria-label="Red pencil"></div>
    <div class="pencil" role="img" aria-label="Red pencil"></div>
    <div class="pencil" role="img" aria-label="Red pencil"></div>
    <div class="pencil" role="img" aria-label="Red pencil"></div>
    <div class="pencil" role="img" aria-label="Red pencil"></div>
    <div class="pencil" role="img" aria-label="Red pencil"></div>
    <div class="pencil" role="img" aria-label="Red pencil"></div>
    <div class="pencil" role="img" aria-label="Red pencil"></div>
    <div class="pencil" role="img" aria-label="Red pencil"></div>
  </div>
  <div class="pencil-row pencil-row--middle">
    <div class="pencil" role="img" aria-label="Red pencil"></div>
    <div class="pencil" role="img" aria-label="Red pencil"></div>
    <div class="pencil" role="img" aria-label="Red pencil"></div>
    <div class="pencil" role="img" aria-label="Red pencil"></div>
    <div class="pencil" role="img" aria-label="Red pencil"></div>
    <div class="pencil" role="img" aria-label="Red pencil"></div>
    <div class="pencil" role="img" aria-label="Red pencil"></div>
    <div class="pencil" role="img" aria-label="Red pencil"></div>
    <div class="pencil" role="img" aria-label="Red pencil"></div>
    <div class="stylus" role="img" aria-label="Black digital drawing stylus standing out among the pencils"></div>
    <div class="pencil" role="img" aria-label="Red pencil"></div>
    <div class="pencil" role="img" aria-label="Red pencil"></div>
  </div>
  <div class="pencil-row pencil-row--bottom">
    <div class="pencil" role="img" aria-label="Red pencil"></div>
    <div class="pencil" role="img" aria-label="Red pencil"></div>
    <div class="pencil" role="img" aria-label="Red pencil"></div>
    <div class="pencil" role="img" aria-label="Red pencil"></div>
    <div class="pencil" role="img" aria-label="Red pencil"></div>
    <div class="pencil" role="img" aria-label="Red pencil"></div>
    <div class="pencil" role="img" aria-label="Red pencil"></div>
    <div class="pencil" role="img" aria-label="Red pencil"></div>
    <div class="pencil" role="img" aria-label="Red pencil"></div>
    <div class="pencil" role="img" aria-label="Red pencil"></div>
    <div class="pencil" role="img" aria-label="Red pencil"></div>
    <div class="pencil" role="img" aria-label="Red pencil"></div>
  </div>
  <p class="caption">Spot me at ArtHarbor</p>
</main>
</body>
</html>
```